Manufacturer of heath beverages and shooters requires label design

We require a label design for our first beverage we are launching in the US market under the brand Meadowra Sipz. Our manufacturing facility is based in California, USA.

The name of the beverage is KorvaTum, and is a health beverage to support gut health. The final design should communicate aspects such as life, energy, nature, well-being, and good health. Logo and dimensions of the label attached.

Target Market(s)

This should appeal to a broad audience across ages and genders. We are targeting individuals who are already health conscious, as well as those who are trying to improve their health.

Industry/Entity Type

Health And Wellness

Requirements
Must have
• Info that must be included
• Attached logo
• The name "KorvaTum"
• Under the name: "Natural digestive aid and overall gut health support"
• An "Organic" icon
• Caffeine-free
• 2 fl oz (59ml)
• Shake well
• Directions:
• Add contents of bottle to 6 oz warm water. Drink first thing in the morning or after a heavy meal. For best results, consume daily.
• Leave space for the nutrition facts and ingredients (will be provided to add to the winning design).
Should not have
• No images of fruit. This is not a fruit beverage.

```html
<!DOCTYPE html>
<html lang="en">
<head>
<meta charset="utf-8">
<title>KorvaTum Label – Meadowra Sipz</title>
<link rel="stylesheet" href="https://fonts.googleapis.com/css2?family=Cabin:wght@400;500;600;700&family=Merienda:wght@400;700&family=Quicksand:wght@400&family=Cinzel:wght@400&display=swap">
<style>
  :root {
    --page: #f6e8e2;
    --band-green: #a8c664;
    --peach-top: #fdc6b2;
    --peach-mid: #fcb68e;
    --peach-low: #f9a154;
    --edge-green: #76bf42;
    --green-top: #8dc95a;
    --green-low: #89c443;
    --ink: #1e1510;
    --heading: #5b4a4d;
    --brand: #ef5b34;
    --tagline: #8c8580;
    --brown: #4a1c0c;
    --badge: #3f5f52;
    --white: #ffffff;
  }
  * { margin: 0; padding: 0; box-sizing: border-box; }
  html, body { width: 1200px; height: 985px; overflow: hidden; background: var(--page); }
  .label { position: relative; width: 1200px; height: 985px; }

  .size-band {
    position: absolute; left: 13px; top: 0; width: 1135px; height: 145px;
    background: var(--band-green); border-radius: 0 0 12px 12px;
    box-shadow: 0 2px 3px rgba(120,90,60,.15);
  }
  .size-band__text {
    position: absolute; left: 222px; top: 14px;
    font: 400 86px/1 "Quicksand", sans-serif;
    color: transparent; -webkit-text-stroke: 2.5px var(--ink);
    letter-spacing: 1px; white-space: nowrap;
  }

  .panel-top {
    position: absolute; left: 17px; top: 145px; width: 1135px; height: 350px;
    background: linear-gradient(180deg, var(--peach-top) 0%, var(--peach-mid) 45%, var(--peach-low) 80%, #f5b363 100%);
  }
  .panel-bottom {
    position: absolute; left: 17px; top: 500px; width: 1135px; height: 485px;
    background: linear-gradient(180deg, var(--green-top) 0%, var(--green-low) 60%, #8bc440 100%);
    border-radius: 0 0 10px 10px;
  }
  .edge-band {
    position: absolute; left: 17px; top: 478px; width: 1135px; height: 24px;
    background: var(--edge-green);
  }

  .side-brand {
    position: absolute; left: 105px; top: 498px;
    transform: translate(-50%, -50%) rotate(90deg);
    font: 700 50px/1 "Merienda", cursive; color: #d8a25c; opacity: .45;
    white-space: nowrap;
  }
  .side-tagline {
    position: absolute; left: 55px; top: 498px;
    transform: translate(-50%, -50%) rotate(90deg);
    font: 400 16px/1 "Cabin", sans-serif; letter-spacing: 9px;
    color: #a6937f; opacity: .45; white-space: nowrap;
  }

  .brand {
    position: absolute; left: 474px; top: 362px; transform: translate(-50%, -50%);
    font: 700 56px/1 "Merienda", cursive; color: var(--brand); white-space: nowrap;
  }
  .brand__tagline {
    position: absolute; left: 474px; top: 425px; transform: translate(-50%, -50%);
    font: 400 21px/1 "Cabin", sans-serif; letter-spacing: 6px;
    color: var(--tagline); white-space: nowrap;
  }

  .product {
    position: absolute; left: 467px; top: 615px; transform: translate(-50%, -50%);
    font: 700 92px/1 "Merienda", cursive; color: var(--white); white-space: nowrap;
  }
  .product__claim {
    position: absolute; left: 478px; top: 663px; transform: translateX(-50%);
    font: 400 18px/30px "Merienda", cursive; text-transform: uppercase;
    color: var(--brown); text-align: center; letter-spacing: .5px; white-space: nowrap;
  }

  .heading {
    position: absolute; left: 793px;
    font: 500 31px/1 "Cabin", sans-serif; color: var(--heading); letter-spacing: .5px;
  }
  .heading--directions { top: 167px; left: 799px; }
  .heading--nutrition { top: 540px; }
  .heading--ingredients { top: 690px; }

  .directions {
    position: absolute; left: 788px; top: 250px; width: 360px;
    font: 500 26.5px/34.5px "Cabin", sans-serif; color: var(--ink); letter-spacing: -1px;
  }

  .volume {
    position: absolute; left: 506px; top: 905px;
    font: 600 23px/1 "Cabin", sans-serif; color: var(--ink); white-space: nowrap;
  }
  .caffeine {
    position: absolute; left: 473px; top: 947px;
    font: 400 21px/1 "Cinzel", serif; color: var(--brown); letter-spacing: 1px; white-space: nowrap;
  }
  .badge { position: absolute; left: 652px; top: 862px; }
  .shake {
    position: absolute; left: 800px; top: 955px;
    font: 400 25px/1 "Cinzel", serif; color: var(--heading); letter-spacing: .5px; white-space: nowrap;
  }
</style>
</head>
<body>
<main class="label">
  <header class="size-band">
    <p class="size-band__text">2 fl oz /59ml</p>
  </header>

  <section class="panel-top"></section>
  <section class="panel-bottom"></section>
  <div class="edge-band" role="img" aria-label="Decorative scalloped green border between the peach and green panels"></div>

  <p class="side-brand">Meadowra Sipz</p>
  <p class="side-tagline">Be Well. Live Well.</p>

  <h1 class="brand">Meadowra Sipz</h1>
  <p class="brand__tagline">Be Well. Live Well.</p>

  <h2 class="heading heading--directions">Directions:</h2>
  <p class="directions">Add contents of bottle to 6 oz<br>warm water. Drink first thing<br>in the morning or after a heavy<br>meal. For best results, consume<br>daily.</p>

  <h2 class="product">KorvaTum</h2>
  <p class="product__claim">Natural digestive aid<br>and overall gut health support</p>

  <h3 class="heading heading--nutrition">Nutrition facts</h3>
  <h3 class="heading heading--ingredients">Ingredients</h3>

  <p class="volume">2 fl oz (59ml)</p>
  <p class="caffeine">Caffeine-free</p>
  <svg class="badge" width="112" height="112" viewBox="0 0 112 112" role="img" aria-label="Organic certification badge">
    <circle cx="56" cy="56" r="56" fill="#3f5f52"/>
  </svg>
  <p class="shake">SHAKE WELL BEFORE USE</p>
</main>
</body>
</html>
```